Business Law Firm Podcast Cover Art

Legal podcast seeking a redesign of our current podcast cover art to match better with our current business' brand profile. You can see our firm's site here: https://www.vorendlegal.com/ And I'm attaching our current podcast cover art. These are based on older photos as well, the newer versions are also attached.

Target Market(s)

business owners

Font styles to use
Serif
Sans Serif

Colors

Designer to choose colors to be used in the design.

Requirements
Must have
• Must have the title "Counsel Clear | Bright Venture".
Nice to have
• Photos of the hosts (Toren & Glen) would be nice, but we are not tied to it.
Should not have
• too small print

```html
<!DOCTYPE html>
<html lang="en">
<head>
<meta charset="utf-8">
<title>Counsel Clear | Bright Venture — Podcast Cover</title>
<link rel="stylesheet" href="https://fonts.googleapis.com/css2?family=Bitter:wght@800&family=Libre+Baskerville&display=swap">
<style>
  :root {
    --blue-deep: #0f7fd6;
    --blue-mid: #1e98ea;
    --blue-light: #45c0f7;
    --ink-navy: #1b1a6b;
    --title-white: #ffffff;
  }
  html, body {
    margin: 0;
    padding: 0;
    width: 1200px;
    height: 1200px;
    overflow: hidden;
  }
  .cover {
    position: relative;
    width: 1200px;
    height: 1200px;
    overflow: hidden;
    background: linear-gradient(160deg, var(--blue-mid) 0%, var(--blue-deep) 45%, var(--blue-mid) 75%, var(--blue-light) 100%);
  }
  .backdrop {
    position: absolute;
    inset: 0;
    background:
      radial-gradient(ellipse 60% 45% at 85% 10%, rgba(120, 215, 255, 0.55), transparent 70%),
      radial-gradient(ellipse 50% 40% at 20% 55%, rgba(10, 90, 170, 0.35), transparent 70%),
      radial-gradient(ellipse 70% 35% at 70% 85%, rgba(90, 200, 250, 0.35), transparent 70%);
  }
  .title-line {
    position: absolute;
    left: 0;
    width: 100%;
    margin: 0;
    text-align: center;
    font-family: "Bitter", Georgia, serif;
    font-weight: 800;
    font-size: 196px;
    line-height: 1;
    letter-spacing: 2px;
    color: var(--title-white);
    text-shadow: 0 4px 10px rgba(0, 40, 100, 0.35);
  }
  .title-line--1 { top: 112px; }
  .title-line--2 { top: 318px; }
  .title-line--3 { top: 618px; }
  .title-line--4 { top: 818px; }
  .divider {
    position: absolute;
    left: 0;
    top: 554px;
    width: 1200px;
    height: 40px;
  }
  .byline {
    position: absolute;
    left: 0;
    top: 1112px;
    width: 100%;
    margin: 0;
    text-align: center;
    font-family: "Libre Baskerville", Georgia, serif;
    font-size: 30px;
    letter-spacing: 7px;
    text-transform: uppercase;
    color: var(--ink-navy);
  }
</style>
</head>
<body>
  <main class="cover">
    <div class="backdrop" role="img" aria-label="Soft blue photo of scales of justice and a gavel behind the title"></div>

    <h1 class="podcast-title" aria-label="Counsel Clear | Bright Venture">
      <span class="title-line title-line--1">COUNSEL</span>
      <span class="title-line title-line--2">CLEAR</span>
      <span class="title-line title-line--3">BRIGHT</span>
      <span class="title-line title-line--4">VENTURE</span>
    </h1>

    <svg class="divider" viewBox="0 0 1200 40" aria-hidden="true">
      <polygon points="176,20 560,16 560,24" fill="var(--ink-navy)"/>
      <polygon points="1024,20 640,16 640,24" fill="var(--ink-navy)"/>
      <circle cx="600" cy="20" r="18" fill="var(--ink-navy)"/>
    </svg>

    <p class="byline">By Toren &amp; Glen</p>
  </main>
</body>
</html>
```